i need a business card for a plumbing company in california

we are a drain cleaning , maintenance plumbing company who is starting new marketing campaign for a tatrench-less pipe installation department .

Target Market(s)

the professional who appreciates time and quality workmanship.

Industry/Entity Type

Plumbing

Colors
0655a3
ec1f27

Requirements
Must have
• the second logo needs to be included
Nice to have
• a focus on the services offered
Should not have
• any underlined words on the brief

```html
<!DOCTYPE html>
<html lang="en">
<head>
<meta charset="utf-8">
<title>Clearline Plumbing – Business Card</title>
<link rel="stylesheet" href="https://fonts.googleapis.com/css2?family=Saira:wght@600&display=swap">
<style>
  :root {
    --card-white: #ffffff;
    --brand-red: #ec1f27;
    --swoosh-grey: #7e7d72;
    --text-grey: #7b7a70;
  }
  html, body {
    margin: 0;
    padding: 0;
    overflow: hidden;
    background: var(--card-white);
  }
  .card {
    position: relative;
    width: 1200px;
    height: 720px;
    overflow: hidden;
    background: var(--card-white);
  }
  .card-swooshes {
    position: absolute;
    inset: 0;
    width: 1200px;
    height: 720px;
  }
  .swoosh-grey { fill: var(--swoosh-grey); }
  .swoosh-red { fill: var(--brand-red); }
  .brand {
    position: absolute;
    left: 0;
    top: 292px;
    width: 1200px;
    display: flex;
    justify-content: center;
    align-items: center;
    gap: 26px;
  }
  .brand-name {
    margin: 0;
    font-family: "Saira", sans-serif;
    font-weight: 600;
    font-size: 72px;
    line-height: 0.98;
    letter-spacing: 0.5px;
    color: var(--text-grey);
    text-align: right;
  }
  .brand-name span { display: block; }
  .brand-square {
    width: 92px;
    height: 92px;
    background: var(--brand-red);
    margin-top: 34px;
  }
</style>
</head>
<body>
  <main class="card">
    <svg class="card-swooshes" viewBox="0 0 1125 675" aria-hidden="true">
      <path class="swoosh-grey" d="M540,0 C850,25 1060,140 1125,262 L1125,0 Z"/>
      <path class="swoosh-red" d="M600,0 C860,15 1045,85 1125,150 L1125,0 Z"/>
      <path class="swoosh-grey" d="M0,418 C80,525 300,640 565,675 L0,675 Z"/>
      <path class="swoosh-red" d="M0,492 C120,585 300,652 470,675 L0,675 Z"/>
    </svg>
    <div class="brand">
      <h1 class="brand-name"><span>Clearline</span><span>Plumbing</span></h1>
      <div class="brand-square" aria-hidden="true"></div>
    </div>
  </main>
</body>
</html>
```